Redesign Craft Brewing Recipe Website

Originally built with Bootstrap just to get the site going, I am seeking a complete redesign of the sites home page and recipe page. I am an experienced web developer with no graphic background, initially just looking for psd mocks.

I prefer styles that are clean and modern, and would prefer anything that is fun, engaging, and has an organic feel to it. I currently have a cartoon rabbit as a logo, but it needs some modification/tweaking, so any help in that area would be great as well.

Current site:
http://kettlefinch.hostgridapps.net/

Current launch page/logo:
http://www.kettlefinch.com/

I like the overall layout of the elements currently, but the design sucks.
Updates

The launch page is at the following URL

Reason: Still looking for a more modern design. Designs received so far are too similar to the original.

My site is content based and does not contain images or products. Your design should not consist of large images.

Reason: The website has very little images, so the designs need to be more text and content based. The header needs to be very small and should not contain an ad rotater.

Target Market(s)

Home brewers, Craft brewers, Microbreweries, Brewpubs

Requirements
Must have
• Web 2.0 Look and Feel, Fun, Hip, Focus on content
Should not have
• A large photo as a header

```html
<!DOCTYPE html>
<html lang="en">
<head>
<meta charset="utf-8">
<title>Kettlefinch – Latest Recipes</title>
<link rel="stylesheet" href="https://fonts.googleapis.com/css2?family=Roboto:wght@300;400;500;700&display=swap">
<style>
:root{
  --page:#f3f3f2;
  --side:#3f3f3f;
  --side-light:#4a4a4a;
  --nav:#4f8b9a;
  --red:#d8433f;
  --blue:#3aa9d4;
  --ink:#3c3c3c;
  --muted:#8c8c8c;
  --white:#ffffff;
  --purple:#b49ad2;
  --green:#9ccc7c;
  --sky:#9cc8d8;
  --grey:#c4c4c4;
}
*{box-sizing:border-box;margin:0;padding:0}
html,body{width:1131px;height:1200px;overflow:hidden;background:var(--page)}
body{font-family:"Roboto",Arial,sans-serif;color:var(--ink)}
.stage{position:relative;width:1200px;height:1273px;transform:scale(.9425);transform-origin:0 0}

/* sidebar */
.sidebar{position:absolute;left:0;top:0;width:367px;height:1217px;
  background:radial-gradient(circle at 50px 130px,rgba(255,255,255,.05) 0 50px,transparent 51px),
  radial-gradient(circle at 150px 180px,rgba(255,255,255,.04) 0 45px,transparent 46px),
  radial-gradient(circle at 280px 20px,rgba(255,255,255,.04) 0 55px,transparent 56px),
  linear-gradient(180deg,var(--side-light),var(--side) 40%);
  color:var(--white)}
.brand{position:absolute;right:24px;top:108px;text-align:left;width:170px}
.brand-mark{position:absolute;left:45px;top:-72px;width:60px;height:60px;border-radius:50%;background:var(--white)}
.brand-name{font-size:33px;font-weight:500;letter-spacing:-.5px;line-height:40px}
.brand-tag{font-size:10px;color:#9a9a9a;line-height:11px;margin-top:1px}
.nav{position:absolute;right:24px;top:207px;display:flex;flex-direction:column;align-items:flex-end;gap:4px;list-style:none}
.nav li{background:var(--nav);color:var(--white);font-size:16px;line-height:24px;padding:0 10px;text-transform:uppercase}
.social{position:absolute;left:250px;top:375px;display:flex;gap:7px}
.social span{width:18px;height:18px;border-radius:2px}
.label{position:absolute;right:29px;font-size:19px;font-weight:300}
.field{position:absolute;left:142px;width:200px;height:28px;background:var(--white);color:#777;font-size:12px;line-height:28px;padding-left:16px}
.field svg{position:absolute;right:14px;top:10px}
.range-title{position:absolute;right:25px;top:743px;font-size:12px;font-weight:500}
.range{position:absolute;left:130px;top:771px;width:213px;height:8px;border-radius:4px;background:var(--white)}
.range-fill{position:absolute;left:57px;width:131px;height:8px;background:#8cc6ea}
.knob{position:absolute;top:-4px;width:11px;height:15px;border-radius:2px;background:#e8e8e8;border:1px solid #aaa}
.ticks{position:absolute;left:130px;top:784px;width:213px;font-size:10px;font-weight:500}
.ticks span{position:absolute;top:8px;transform:translateX(-50%)}
.ticks i{position:absolute;top:0;width:1px;height:5px;background:#bbb}
.update{position:absolute;left:217px;top:841px;width:128px;height:30px;background:var(--white);border:1px solid #ccc;color:#333;font-size:13px;font-weight:500;line-height:28px;text-align:center}

/* main */
.title{position:absolute;left:388px;top:108px;font-size:34px;font-weight:700;color:var(--red);letter-spacing:-1px}
.tabs{position:absolute;left:392px;top:161px;font-size:15px;color:#9a9a9a}
.tabs b{font-weight:400;color:#222}
.tabs em{font-style:normal;margin:0 10px;color:#555}
.grid{position:absolute;left:392px;top:205px;display:grid;grid-template-columns:330px 330px;grid-auto-rows:210px;column-gap:30px;row-gap:32px}
.card{position:relative;background:var(--white);box-shadow:0 1px 2px rgba(0,0,0,.06)}
.card::before{content:"";position:absolute;left:0;top:0;width:4px;height:171px;background:var(--accent)}
.card::after{content:"";position:absolute;left:-6px;top:27px;border:6px solid transparent;border-right-color:var(--accent);border-left:0}
.card.purple{--accent:var(--purple)}.card.green{--accent:var(--green)}.card.sky{--accent:var(--sky)}.card.grey{--accent:var(--grey)}
.thumb{position:absolute;left:20px;top:10px;width:86px;height:88px;border:1px solid #e2e2e2;
  background:linear-gradient(90deg,#fff 0 14px,#7c8a2a 14px 28px,#fff 28px 36px,#b8282d 36px 50px,#fff 50px 58px,#2a2224 58px 72px,#fff 72px)}
.tag{position:absolute;left:20px;width:86px;height:24px;color:var(--white);font-size:13px;font-weight:500;line-height:24px;text-align:center}
.tag.extract{top:107px;background:var(--red)}
.tag.style{top:135px;background:var(--blue)}
.name{position:absolute;left:121px;top:16px;font-size:19px;font-weight:300;color:#333;letter-spacing:-.3px;word-spacing:2px}
.byline{position:absolute;left:121px;top:47px;font-size:12px;color:#333}
.byline span{color:var(--blue)}
.blurb{position:absolute;left:121px;top:71px;width:196px;font-size:11px;line-height:18px;color:var(--muted)}
.stats{position:absolute;left:0;bottom:0;width:330px;height:40px;display:flex;list-style:none}
.stats li{width:66px;background:var(--blue);color:var(--white);font-size:12px;font-weight:500;line-height:13px;text-align:center;padding-top:7px;border-right:1px solid rgba(255,255,255,.35)}
.stats li:last-child{background:var(--red);border-right:0}
.results{position:absolute;left:391px;top:1162px;width:690px;height:55px;background:#000;color:var(--white);font-size:14px;font-weight:500}
.results .r1{position:absolute;left:17px;top:19px}
.results .r2{position:absolute;left:155px;top:19px}
.pager{position:absolute;top:16px;height:23px;background:var(--white);color:#333;font-size:11px;line-height:23px;text-align:center}
.footer{position:absolute;right:131px;top:1238px;font-size:12px;color:#444}
</style>
</head>
<body>
<div class="stage">
  <aside class="sidebar">
    <div class="brand">
      <span class="brand-mark"></span>
      <div class="brand-name">Kettlefinch</div>
      <div class="brand-tag">Easiest way to create and share craft beer recipes.</div>
    </div>
    <ul class="nav">
      <li>Home</li><li>Recipes</li><li>About Us</li><li>Our Clients</li><li>Contact</li>
    </ul>
    <div class="social">
      <span style="background:#4aa8dc"></span><span style="background:#3b5b9c"></span><span style="background:#2a2a2a"></span><span style="background:#f08a1c"></span>
    </div>
    <div class="label" style="top:423px">Search Recipes</div>
    <div class="field" style="top:453px">Stout</div>
    <div class="label" style="top:499px">Match Maker</div>
    <div class="field" style="top:530px">Boil Size
      <svg width="9" height="9" viewBox="0 0 9 9"><circle cx="4.5" cy="4.5" r="4" fill="none" stroke="#999"/><circle cx="4.5" cy="4.5" r="2" fill="#333"/></svg></div>
    <div class="label" style="top:576px">Brewing</div>
    <div class="field" style="top:607px">Extract
      <svg width="9" height="6" viewBox="0 0 9 6"><path d="M0 0h9L4.5 6z" fill="#444"/></svg></div>
    <div class="label" style="top:653px">Styles</div>
    <div class="field" style="top:684px">American Amber Ale
      <svg width="9" height="6" viewBox="0 0 9 6"><path d="M0 0h9L4.5 6z" fill="#444"/></svg></div>
    <div class="range-title">0 Gals to 25 Gals</div>
    <div class="range"><div class="range-fill"></div><span class="knob" style="left:52px"></span><span class="knob" style="left:183px"></span></div>
    <div class="ticks">
      <i style="left:7px"></i><i style="left:45px"></i><i style="left:85px"></i><i style="left:123px"></i><i style="left:162px"></i><i style="left:200px"></i>
      <span style="left:7px">0</span><span style="left:45px">5</span><span style="left:85px">10</span><span style="left:123px">15</span><span style="left:162px">20</span><span style="left:200px">25</span>
    </div>
    <div class="update">UPDATE SEARCH</div>
  </aside>

  <h1 class="title">Latest Recipes</h1>
  <div class="tabs">Popular<em>/</em><b>Recent</b></div>

  <main class="grid">
    <article class="card purple"><div class="thumb" role="img" aria-label="Three wine bottles: green, red and dark"></div><div class="tag extract">Extract</div><div class="tag style">Sweet Mead</div><h2 class="name">Oak Bastard Sweet Mead</h2><p class="byline"><span>Created by</span> Marten Hale</p><p class="blurb">Le Lorem Ipsum est simplement du faux texte employé dans la composition mise en page avant impression. Lorem Ipsum est le faux texte merie depuis les années 1500.</p><ul class="stats"><li>1.022<br>og</li><li>1.006<br>fb</li><li>24<br>ibu</li><li>2.24%<br>abv</li><li>9<br>SRM</li></ul></article>
    <article class="card purple"><div class="thumb" role="img" aria-label="Three wine bottles: green, red and dark"></div><div class="tag extract">Extract</div><div class="tag style">Sweet Mead</div><h2 class="name">Oak Bastard Sweet Mead</h2><p class="byline"><span>Created by</span> Marten Hale</p><p class="blurb">Le Lorem Ipsum est simplement du faux texte employé dans la composition mise en page avant impression. Lorem Ipsum est le faux texte merie depuis les années 1500.</p><ul class="stats"><li>1.022<br>og</li><li>1.006<br>fb</li><li>24<br>ibu</li><li>2.24%<br>abv</li><li>9<br>SRM</li></ul></article>
    <article class="card green"><div class="thumb" role="img" aria-label="Three wine bottles: green, red and dark"></div><div class="tag extract">Extract</div><div class="tag style">Sweet Mead</div><h2 class="name">Oak Bastard Sweet Mead</h2><p class="byline"><span>Created by</span> Marten Hale</p><p class="blurb">Le Lorem Ipsum est simplement du faux texte employé dans la composition mise en page avant impression. Lorem Ipsum est le faux texte merie depuis les années 1500.</p><ul class="stats"><li>1.022<br>og</li><li>1.006<br>fb</li><li>24<br>ibu</li><li>2.24%<br>abv</li><li>9<br>SRM</li></ul></article>
    <article class="card green"><div class="thumb" role="img" aria-label="Three wine bottles: green, red and dark"></div><div class="tag extract">Extract</div><div class="tag style">Sweet Mead</div><h2 class="name">Oak Bastard Sweet Mead</h2><p class="byline"><span>Created by</span> Marten Hale</p><p class="blurb">Le Lorem Ipsum est simplement du faux texte employé dans la composition mise en page avant impression. Lorem Ipsum est le faux texte merie depuis les années 1500.</p><ul class="stats"><li>1.022<br>og</li><li>1.006<br>fb</li><li>24<br>ibu</li><li>2.24%<br>abv</li><li>9<br>SRM</li></ul></article>
    <article class="card sky"><div class="thumb" role="img" aria-label="Three wine bottles: green, red and dark"></div><div class="tag extract">Extract</div><div class="tag style">Sweet Mead</div><h2 class="name">Oak Bastard Sweet Mead</h2><p class="byline"><span>Created by</span> Marten Hale</p><p class="blurb">Le Lorem Ipsum est simplement du faux texte employé dans la composition mise en page avant impression. Lorem Ipsum est le faux texte merie depuis les années 1500.</p><ul class="stats"><li>1.022<br>og</li><li>1.006<br>fb</li><li>24<br>ibu</li><li>2.24%<br>abv</li><li>9<br>SRM</li></ul></article>
    <article class="card sky"><div class="thumb" role="img" aria-label="Three wine bottles: green, red and dark"></div><div class="tag extract">Extract</div><div class="tag style">Sweet Mead</div><h2 class="name">Oak Bastard Sweet Mead</h2><p class="byline"><span>Created by</span> Marten Hale</p><p class="blurb">Le Lorem Ipsum est simplement du faux texte employé dans la composition mise en page avant impression. Lorem Ipsum est le faux texte merie depuis les années 1500.</p><ul class="stats"><li>1.022<br>og</li><li>1.006<br>fb</li><li>24<br>ibu</li><li>2.24%<br>abv</li><li>9<br>SRM</li></ul></article>
    <article class="card grey"><div class="thumb" role="img" aria-label="Three wine bottles: green, red and dark"></div><div class="tag extract">Extract</div><div class="tag style">Sweet Mead</div><h2 class="name">Oak Bastard Sweet Mead</h2><p class="byline"><span>Created by</span> Marten Hale</p><p class="blurb">Le Lorem Ipsum est simplement du faux texte employé dans la composition mise en page avant impression. Lorem Ipsum est le faux texte merie depuis les années 1500.</p><ul class="stats"><li>1.022<br>og</li><li>1.006<br>fb</li><li>24<br>ibu</li><li>2.24%<br>abv</li><li>9<br>SRM</li></ul></article>
    <article class="card grey"><div class="thumb" role="img" aria-label="Three wine bottles: green, red and dark"></div><div class="tag extract">Extract</div><div class="tag style">Sweet Mead</div><h2 class="name">Oak Bastard Sweet Mead</h2><p class="byline"><span>Created by</span> Marten Hale</p><p class="blurb">Le Lorem Ipsum est simplement du faux texte employé dans la composition mise en page avant impression. Lorem Ipsum est le faux texte merie depuis les années 1500.</p><ul class="stats"><li>1.022<br>og</li><li>1.006<br>fb</li><li>24<br>ibu</li><li>2.24%<br>abv</li><li>9<br>SRM</li></ul></article>
  </main>

  <div class="results">
    <span class="r1">Search Result</span><span class="r2">12 Found</span>
    <span class="pager" style="left:566px;width:47px">Prev</span>
    <span class="pager" style="left:626px;width:46px">Next</span>
  </div>
  <p class="footer">Copyright 2013 Website Name. All Rights Reserved.</p>
</div>
</body>
</html>
```